Branding website for a Data Science company with 1 product

Branding website for a Data Science company, featuring our main product: Quorlink. The purpose of the website is to get potential clients to get a peek at what we do, but the main purpose is to get them to get in touch with us. The website will not answer all questions. Therefore the contact details and contact form is a must-have .

Target Market(s)

Potential new B2B clients with medium to large websites, application users (behind a login)

Industry/Entity Type

It Company

Coding

Coded - Design and coding required

Number of Pages Required

2 page

Font styles to use
Sans Serif

Colors

Designer to choose colors to be used in the design.

Requirements
Must have
• A contact form and branding a product

```html
<!DOCTYPE html>
<html lang="en">
<head>
<meta charset="utf-8">
<title>Vexel Partners – Data Science</title>
<link href="https://fonts.googleapis.com/css2?family=Open+Sans+Condensed:wght@300&family=Roboto+Condensed:wght@400;700&family=Questrial&display=swap" rel="stylesheet">
<style>
:root{
  --orange:#f05a28;
  --orange-deep:#d9481c;
  --ink:#111111;
  --night:#0b1219;
  --night-2:#17222d;
  --white:#ffffff;
  --grey-text:#9a9a9a;
  --line:#e6e6e6;
}
*{box-sizing:border-box;margin:0;padding:0}
html,body{width:1200px;height:3579px;overflow:hidden}
body{font-family:"Questrial",sans-serif;color:var(--white);background:var(--white);position:relative}
section,header,footer{position:absolute;left:0;width:1200px;overflow:hidden}
.fill{position:absolute;inset:0}
.heading{font-family:"Roboto Condensed",sans-serif;font-weight:400;font-size:40px;text-align:center;letter-spacing:.5px}
.heading .accent{color:var(--orange)}
.subheading{font-size:15px;text-align:center}

/* hero */
.hero{top:0;height:680px;background:var(--night)}
.hero .fill{background:radial-gradient(ellipse at 50% 95%,#2c4a66 0%,#14263a 35%,#070c12 75%)}
.brand{position:absolute;left:79px;top:34px;display:flex;align-items:center;gap:14px}
.brand-dot{width:56px;height:56px;border-radius:50%;background:var(--orange)}
.brand-name{font-family:"Questrial",sans-serif;font-size:30px;color:var(--white);line-height:1;letter-spacing:2px}
.nav{position:absolute;top:43px;left:456px;display:flex;align-items:center;font-size:16px}
.nav a{color:var(--white);text-decoration:none;height:48px;line-height:48px}
.nav .home{background:var(--orange);border-radius:24px;padding:0 22px;margin-right:30px}
.nav a+a{margin-left:0}
.nav .n2{margin-right:30px}
.hero-title{position:absolute;top:280px;left:0;width:100%;text-align:center;font-family:"Open Sans Condensed",sans-serif;font-weight:300;font-size:46px;line-height:62px}
.play{position:absolute;left:548px;top:444px}

/* welcome */
.welcome{top:680px;height:310px;background:var(--orange)}
.welcome .heading{margin-top:56px;color:var(--ink)}
.welcome .heading .accent{color:var(--white)}
.welcome .subheading{color:var(--ink);margin-top:2px}
.welcome p{width:870px;margin:18px auto 0;text-align:center;font-size:15px;line-height:26px}
.chev{position:absolute;left:590px;top:922px;top:242px}

/* services */
.services{top:990px;height:518px;background:var(--night)}
.services .fill{background:linear-gradient(180deg,#0c151e 0%,#1a2836 50%,#0c141c 100%)}
.services .heading{position:relative;margin-top:62px}
.services .subheading{position:relative;color:#cfd6dc}
.cards{position:absolute;top:191px;left:79px;display:flex;gap:17px}
.card{width:248px;height:260px;position:relative;background:#e9e9e9}
.card.advisory{background:var(--orange);padding:22px 14px}
.card.advisory h3{font-family:"Roboto Condensed",sans-serif;font-weight:700;font-size:19px;color:var(--ink);text-align:center;margin-bottom:10px}
.card.advisory p{font-size:14px;line-height:23px;color:var(--white)}
.card .art{position:absolute;left:0;top:0;width:248px;height:198px;background:linear-gradient(180deg,#f2f2f2,#d6d6d6)}
.card .bar{position:absolute;left:0;bottom:0;width:248px;height:62px;background:#1b1b1b;color:var(--orange);font-family:"Roboto Condensed",sans-serif;font-size:17px;line-height:62px;padding-left:12px;text-transform:uppercase}
.card .bar::before{content:"";display:inline-block;width:20px;height:2px;background:var(--orange);vertical-align:middle;margin-right:16px}
.arrow{position:absolute;top:300px}

/* product */
.product{top:1508px;height:344px;background:var(--white);color:var(--ink)}
.product .heading{margin-top:56px}
.product .subheading{margin-top:2px}
.product p{width:820px;margin:16px auto 0;text-align:center;color:var(--grey-text);font-size:14px;line-height:26px}
.product p+p{margin-top:8px}

/* feature */
.feature{top:1852px;height:479px}
.feature ul{position:absolute;right:85px;top:188px;list-style:none;text-align:right;font-size:15px}
.feature li{height:35.3px;line-height:35.3px}
.feature li::after{content:"";display:inline-block;width:9px;height:9px;border-radius:50%;background:var(--ink);margin-left:14px;vertical-align:middle}
.feature .heading{position:absolute;right:79px;top:120px;text-align:right;color:var(--white)}
.feature .heading .accent{color:var(--white)}

/* partners */
.partners{top:2331px;height:425px;background:var(--white);color:var(--ink)}
.partners .heading{margin-top:56px}
.partner-grid{position:absolute;left:228px;top:127px;display:grid;grid-template-columns:repeat(3,248px);grid-template-rows:repeat(2,120px)}
.partner-cell{display:flex;align-items:center;justify-content:center;border-right:1px solid var(--line);border-bottom:1px solid var(--line)}
.partner-cell:nth-child(3n){border-right:none}
.partner-cell:nth-child(n+4){border-bottom:none}
.partner-badge{width:180px;height:42px;border-radius:4px;background:#3a3a3a}

/* contact */
.contact{top:2756px;height:298px;background:var(--orange);text-align:center;overflow:visible;z-index:2}
.contact .heading{margin-top:44px;color:var(--ink)}
.contact .heading .accent{color:var(--white)}
.contact .phone{font-size:21px;font-weight:700;margin-top:14px;font-family:"Roboto Condensed",sans-serif}
.contact .line{font-size:16px;margin-top:14px}
.notch{position:absolute;left:584px;bottom:-16px}

/* form */
.form-area{top:3054px;height:465px;background:var(--night)}
.form-area .fill{background:linear-gradient(180deg,#1c1f24 0%,#2b3038 50%,#14171b 100%)}
.contact-form{position:absolute;left:353px;top:0;width:494px}
.field{display:block;border-bottom:1px solid rgba(255,255,255,.25);font-size:13px;color:#d8d8d8;padding-top:14px;height:58px}
.field.message{height:132px;position:relative}
.field.message::after{content:"";position:absolute;right:4px;bottom:6px;width:8px;height:8px;border-right:1px solid #aaa;border-bottom:1px solid #aaa}
.submit{position:absolute;left:170px;top:346px;width:155px;height:55px;border-radius:28px;background:var(--orange);color:var(--white);font-family:"Roboto Condensed",sans-serif;font-size:18px;border:none;text-transform:uppercase}

/* footer */
.site-footer{top:3519px;height:60px;background:var(--orange);text-align:center;line-height:60px;font-size:14px}
</style>
</head>
<body>

<header class="hero">
  <div class="fill" role="img" aria-label="Night view of a glowing digital globe with network lines"></div>
  <div class="brand"><span class="brand-dot"></span><span class="brand-name">VEXEL PARTNERS</span></div>
  <nav class="nav">
    <a class="home" href="#">HOME</a>
    <a href="#" style="margin-right:30px">ABOUT</a>
    <a href="#" style="margin-right:30px">WHO WE ARE</a>
    <a href="#" style="margin-right:30px">WHAT WE DO</a>
    <a href="#" style="margin-right:30px">OUR PRODUCT</a>
    <a href="#">CONTACT</a>
  </nav>
  <h1 class="hero-title" style="font-weight:300">Quorlink is Our on-Demand, Software-as-a-Service<br>Real-Time Streaming Data Platform</h1>
  <svg class="play" width="104" height="104" viewBox="0 0 104 104" aria-label="Play video">
    <circle cx="52" cy="52" r="48" fill="none" stroke="#f05a28" stroke-width="6"/>
    <polygon points="40,30 76,52 40,74" fill="#f05a28"/>
  </svg>
</header>

<section class="welcome">
  <h2 class="heading">WELCOME TO <span class="accent">VEXEL PARTNERS</span></h2>
  <div class="subheading">Who We Are</div>
  <p>We believe that every company needs data science and algorithms to stay on top of today's overwhelming speed of innovation. We advise and help to turn your company into a data driven company by making data science comprehensible and usable for everybody in your organization.</p>
  <svg class="chev" width="20" height="16" viewBox="0 0 20 16"><path d="M3 2l7 6 7-6M3 8l7 6 7-6" fill="none" stroke="#7a2a10" stroke-width="2"/></svg>
</section>

<section class="services">
  <div class="fill" role="img" aria-label="Dark background of streaming binary code"></div>
  <h2 class="heading"><span class="accent">OUR</span> SERVICES</h2>
  <div class="subheading">What We Do</div>
  <svg class="arrow" style="left:28px" width="18" height="60" viewBox="0 0 18 60"><path d="M15 2L3 30l12 28" fill="none" stroke="#fff" stroke-width="2"/></svg>
  <svg class="arrow" style="left:1154px" width="18" height="60" viewBox="0 0 18 60"><path d="M3 2l12 28L3 58" fill="none" stroke="#fff" stroke-width="2"/></svg>
  <div class="cards">
    <div class="card advisory">
      <h3>ADVISORY</h3>
      <p>Data science comes in many flavors. Which one fits your company best? Taking all costs, benefits &amp; organizational impact into account? We can help you with formulating a strategy to make sure you get the most out of your data.</p>
    </div>
    <div class="card">
      <div class="art" role="img" aria-label="Illustration of a hand holding a lightbulb with idea icons"></div>
      <div class="bar">Insights</div>
    </div>
    <div class="card">
      <div class="art" role="img" aria-label="Illustration of a laptop surrounded by data icons"></div>
      <div class="bar">Data Engineering</div>
    </div>
    <div class="card">
      <div class="art" role="img" aria-label="Illustration of a security shield with a padlock and documents"></div>
      <div class="bar">Data Privacy &amp; Security</div>
    </div>
  </div>
</section>

<section class="product">
  <h2 class="heading">OUR <span class="accent">PRODUCT</span></h2>
  <div class="subheading">Quorlink</div>
  <p>Quorlink is our on-demand, software-as-a-service real-time streaming data platform. You can use it to capture, analyze, profile and target your customers. The setup can be done in minutes, which prevents lengthy and costly implementation times.</p>
  <p>And all data will come in your own data warehouse. Quorlink is a combination of proven and disruptive technologies to ensure you work with the greatest in streaming and real-time. The 100% online reporting interface gives immediate access to the dashboards from any device or location.</p>
</section>

<section class="feature">
  <svg class="fill" width="1200" height="479" viewBox="0 0 1200 479">
    <defs>
      <linearGradient id="featurePhoto" x1="0" y1="0" x2="1" y2="1">
        <stop offset="0" stop-color="#1a2f45"/>
        <stop offset="0.6" stop-color="#0b1620"/>
        <stop offset="1" stop-color="#050a0f"/>
      </linearGradient>
      <linearGradient id="featureOrange" x1="0" y1="0" x2="1" y2="1">
        <stop offset="0" stop-color="#f26a34"/>
        <stop offset="1" stop-color="#e7521f"/>
      </linearGradient>
    </defs>
    <rect width="1200" height="479" fill="url(#featurePhoto)" role="img" aria-label="Hand holding a smartphone in front of glowing network lines"/>
    <polygon points="632,0 1200,0 1200,479 406,479" fill="url(#featureOrange)"/>
  </svg>
  <h2 class="heading">PRODUCT <span class="accent">FEATURE</span></h2>
  <ul>
    <li>Works on your own database</li>
    <li>Real-time website visitor tracking</li>
    <li>Real-time profiling</li>
    <li>Real-time recommendations</li>
    <li>Create all your reports online with simple drag &amp; drop</li>
    <li>Agile data abstraction layer turns data into Key Performance Indicators</li>
    <li>Automated data gathering from all data sources</li>
  </ul>
</section>

<section class="partners">
  <h2 class="heading">OUR <span class="accent">PARTNER</span></h2>
  <div class="partner-grid">
    <div class="partner-cell"><span class="partner-badge"></span></div>
    <div class="partner-cell"><span class="partner-badge"></span></div>
    <div class="partner-cell"><span class="partner-badge"></span></div>
    <div class="partner-cell"><span class="partner-badge"></span></div>
    <div class="partner-cell"><span class="partner-badge"></span></div>
    <div class="partner-cell"><span class="partner-badge"></span></div>
  </div>
</section>

<section class="contact">
  <h2 class="heading">CONTACT <span class="accent">US</span></h2>
  <div class="phone">31 600 123 456</div>
  <div class="line">hello@vexelpartners.com</div>
  <div class="line">www.vexelpartners.com</div>
  <div class="line">VEXEL PARTNERS Amsterdam / Netherlands</div>
  <svg class="notch" width="32" height="17" viewBox="0 0 32 17"><polygon points="0,0 32,0 16,16" fill="#f05a28"/></svg>
</section>

<section class="form-area">
  <div class="fill" role="img" aria-label="Dimmed photo of hands typing on a keyboard"></div>
  <form class="contact-form">
    <label class="field">Name*</label>
    <label class="field">Email*</label>
    <label class="field">Phone*</label>
    <label class="field message">Message*</label>
    <button class="submit" type="button">Submit</button>
  </form>
</section>

<footer class="site-footer">©VEXEL PARTNERS - 2017 All rights reserved.</footer>

</body>
</html>
```